Cover for Small sparks Make Small Fires

Book Cover Request
Format: Print and electronic (Bookvale)
Book Title: Small Sparks Make Small Fires: Practical Roadmap for Momentum and Purpose
Author: R.K. Vandemeer
Description: This self-help book, written by me, a self-proclaimed nobody, is filled with actionable insights and proven strategies that can help anyone. It combines humor with a serious undertone to deliver practical advice without the typical "self-helpy" vibe.
Catchphrase for the Cover: "Go from Oh Shit to Crushing It!" (or something similar)
Style: I want the cover to reflect my personality—funny, yet serious when needed. I'm open to suggestions and would love to see a design that captures the essence of the book without being too typical of the self-help genre.
Additional Information: I've attached a rough draft of the Bookvale description for more context.
Thank you for your help!
Target Market(s)
Anyone. but id say over 25
Requirements
Nice to have
- Honestly im really at a loss. Im hoping the description will help guide you. I gues i would like it to satand out of course. Be diffrent....but i know how crazy that sounds because everyone wants that. Just give me soem ideas!

```html
<!DOCTYPE html>
<html lang="en">
<head>
<meta charset="utf-8">
<title>Small Sparks Make Small Fires — Cover</title>
<link href="https://fonts.googleapis.com/css2?family=Roboto+Condensed:wght@700&family=Carlito&family=Cinzel:wght@700&display=swap" rel="stylesheet">
<style>
  :root {
    --backdrop: #a1a1a1;
    --paper: #ffffff;
    --ember: #ec6b4f;
    --ember-tint: #f8ddd4;
    --charcoal: #352b2a;
    --charcoal-tint: #e6e2e1;
    --haze: #f1f1f1;
    --ink: #2b2524;
  }
  * { margin: 0; padding: 0; box-sizing: border-box; }
  html, body {
    width: 1200px; height: 1061px; overflow: hidden;
    background: var(--backdrop);
  }
  .cover-frame {
    position: absolute; left: 250px; top: 36px;
    width: 700px; height: 989px; overflow: hidden;
  }
  .cover {
    position: absolute; left: 0; top: 0;
    width: 876px; height: 1238px;
    background: var(--paper);
    transform: scale(0.7991);
    transform-origin: top left;
    overflow: hidden;
  }
  .title {
    position: absolute; left: 126px; top: 140px;
    font-family: "Roboto Condensed", "Arial Narrow", sans-serif;
    font-weight: 700; font-size: 66px; line-height: 53px;
    color: var(--ember); letter-spacing: 1px;
  }
  .subtitle {
    position: absolute; left: 127px; top: 272px;
    font-family: "Carlito", "Calibri", sans-serif;
    font-size: 39px; line-height: 37px;
    color: var(--ink); letter-spacing: 0.6px;
  }
  .backdrop-field {
    position: absolute; left: 366px; top: 627px;
    width: 510px; height: 505px;
    background: radial-gradient(circle at 0 0, var(--paper) 0%, var(--haze) 60%, var(--paper) 100%);
  }
  .tile {
    position: absolute; width: 122px; height: 122px;
  }
  .tile--ember { background: var(--ember); }
  .tile--charcoal { background: var(--charcoal); }
  .tile--ember-tint { background: var(--ember-tint); }
  .tile--charcoal-tint { background: var(--charcoal-tint); }
  .tagline-band {
    position: absolute; left: 366px; top: 506px;
    width: 510px; height: 121px;
    background: var(--charcoal);
  }
  .tagline {
    position: absolute; left: 65px; top: 22px;
    font-family: "Cinzel", "Copperplate", serif;
    font-weight: 700; font-size: 34px; line-height: 40px;
    color: var(--paper); letter-spacing: 1.5px;
  }
  .author {
    position: absolute; right: 86px; top: 1161px;
    font-family: "Cinzel", "Copperplate", serif;
    font-weight: 700; font-size: 15px;
    color: var(--ink); letter-spacing: 1px;
  }
</style>
</head>
<body>
  <div class="cover-frame">
    <main class="cover">
      <div class="backdrop-field" role="img" aria-label="Faint grey concentric arc pattern radiating from the tile grid"></div>

      <h1 class="title">Small Sparks Make<br>Small Fires</h1>
      <p class="subtitle">Practical Roadmap for<br>Momentum and Purpose</p>

      <div class="tile-grid" role="img" aria-label="Mosaic of square tiles with concentric quarter-circle arcs in orange, charcoal and white">
        <div class="tile tile--ember" style="left:122px;top:506px"></div>
        <div class="tile tile--ember-tint" style="left:244px;top:506px"></div>
        <div class="tile tile--charcoal" style="left:0;top:627px"></div>
        <div class="tile tile--ember" style="left:122px;top:627px"></div>
        <div class="tile tile--charcoal-tint" style="left:244px;top:627px"></div>
        <div class="tile tile--charcoal-tint" style="left:122px;top:749px"></div>
        <div class="tile tile--ember" style="left:244px;top:749px"></div>
        <div class="tile tile--charcoal" style="left:244px;top:871px"></div>
        <div class="tile tile--charcoal" style="left:122px;top:993px"></div>
        <div class="tile tile--charcoal" style="left:244px;top:993px"></div>
        <div class="tile tile--charcoal" style="left:244px;top:1115px;height:123px"></div>
      </div>

      <div class="tagline-band">
        <p class="tagline">Go from Oh Shit<br>to Crushing It!</p>
      </div>

      <p class="author">Author: R.K. Vandemeer</p>
    </main>
  </div>
</body>
</html>
```